Etiketten-Design für Nahrungsergänzungsmittel gesucht
Zielgruppe
Verkauf von Nahrungsergänzungsmittel, Magnesium, OPC, Vitamin C …….
18+ Jahre Online- Kunden
Aufgabenstellung
Aufgabenstellung:
Etikettendesign
Für unsere Eigenmarke ˮvelquoraˮ suchen wir ein Etikett.
Ein Logo haben wir bereits erstellen lassen.
Siehe Datei: Logo
Die Schriftart vom Logo finden wir sehr gut, die zwei kleinen Blätter auf dem Logo können auch rausgenommen (falls es nicht zum Etikettendesign passt) werden und mit einem Punkt oder Strich ersetzt werden, sind aber offen auch für andere Ideen. Das Schriftlogo (Wortmarke) bitte in Schwarz und kleingeschrieben.
Bei Logo bitte noch das ® (R im Kreis) für „Registered“ Markenschutz“ hinzufügen, wurde vergessen.
Das Etikett soll hochwertig und modern wirken
Bitte keine Bilder von Kapseln oder Früchte…….
Die Farbe des Etiketts bitte in Weiß
Hier sind einige Beispiele was wir gut finden….
https://torvexhealth.com/collections/immune-system-supplements
https://www.brelmonkraft.de/
https://www.quellsinn.de/
Da wir unsere Produkte hauptsächlich über Dorvaxo FBA verkaufen werden,
sollte sich das Design des Etiketts sich von der Konkurrenz abheben mit einem hohen Wiedererkennungswert.
Das Produkt soll im Vordergrund stehen, das Logo (velquora) im Hintergrund.
Außerdem soll das Etikett auch anpassbar sein, dass wir selbst die Maße des Etiketts sowie Produkttitel, Verzehrempfehlung, Zutaten, Nährwerte, Nahrungsergänzungsmittel mit, Kapsel / Tablettenmenge sowie Sorgfältig hergestellt für,ˮ ändern können. Schön wäre es auch wenn wir die Farben des Bildes oder der Vitaminen ändern können je nach Produkt, ohne das sich Grunddesign ändert.
Wichtig ist:
Platz einplanen für Strichcode und dass alle geforderten Pflichtangaben auf dem Etikett stehen müssen. (siehe Fotos /Word Datei)
Bitte beachten, dass die Schriftgröße von den Pflichtangaben Links und Rechts min.1,2mm groß sind.
Die Pet Dose sowie der Deckel wird in einem Dunkelbraun oder Schwarz sein (siehe Foto).
Das Design soll auch passend für Doypack Tüte..

```html
<!DOCTYPE html>
<html lang="de">
<head>
<meta charset="UTF-8">
<title>velquora Magnesium Komplex – Etikett</title>
<link href="https://fonts.googleapis.com/css2?family=Comfortaa:wght@300;400&family=Oswald:wght@500&display=swap" rel="stylesheet">
<style>
  :root {
    --backdrop: #ededed;
    --label-white: #ffffff;
    --teal: #2fb8c3;
    --teal-light: #4cc6cf;
    --teal-dark: #1fa2ad;
    --title-grey: #8c8f91;
    --logo-black: #2a2a2a;
    --ornament-grey: #e1e4e5;
    --badge-grey: #6f7274;
  }
  * { margin: 0; padding: 0; box-sizing: border-box; }
  html, body {
    width: 1200px;
    height: 900px;
    overflow: hidden;
    background: var(--backdrop);
  }
  .canvas {
    position: relative;
    width: 1200px;
    height: 900px;
  }
  .pouch-label {
    position: absolute;
    left: 400px;
    top: 150px;
    width: 400px;
    height: 600px;
    background: var(--label-white);
    overflow: hidden;
    border-radius: 4px;
  }
  .band-top {
    position: absolute;
    left: 0; top: 0;
    width: 100%;
    height: 180px;
    background: linear-gradient(180deg, var(--teal-light) 0%, var(--teal) 55%, var(--teal-dark) 100%);
  }
  .zip-line {
    position: absolute;
    left: 0;
    width: 100%;
    height: 2px;
    background: rgba(255,255,255,0.35);
  }
  .zip-line.first { top: 62px; }
  .zip-line.second { top: 70px; }
  .band-bottom {
    position: absolute;
    left: 0; bottom: 0;
    width: 100%;
    height: 62px;
    background: linear-gradient(180deg, var(--teal-light) 0%, var(--teal) 100%);
  }
  .brand-mark {
    position: absolute;
    top: 200px;
    right: 30px;
    font-family: 'Comfortaa', sans-serif;
    font-weight: 400;
    font-size: 12px;
    color: var(--logo-black);
    letter-spacing: 0.2px;
  }
  .brand-mark sup { font-size: 7px; }
  .product-title {
    position: absolute;
    top: 230px;
    left: 0;
    width: 100%;
    text-align: center;
    font-family: 'Comfortaa', sans-serif;
    font-weight: 300;
    font-size: 42px;
    line-height: 1.22;
    color: var(--title-grey);
  }
  .product-title .line-two { display: block; padding-right: 40px; }
  .flower-ornament {
    position: absolute;
    top: 350px;
    left: 140px;
    width: 130px;
    height: 125px;
    background: radial-gradient(circle, var(--ornament-grey) 0%, var(--ornament-grey) 55%, rgba(225,228,229,0) 72%);
    border-radius: 50%;
  }
  .vegan-badge {
    position: absolute;
    left: 26px;
    bottom: 82px;
    width: 30px;
    height: 30px;
    border: 2px solid var(--badge-grey);
    border-radius: 50%;
  }
  .capsule-count {
    position: absolute;
    right: 26px;
    bottom: 84px;
    font-family: 'Oswald', sans-serif;
    font-weight: 500;
    font-size: 11px;
    letter-spacing: 0.6px;
    color: #555;
  }
</style>
</head>
<body>
  <main class="canvas">
    <section class="pouch-label">
      <div class="band-top">
        <span class="zip-line first"></span>
        <span class="zip-line second"></span>
      </div>

      <div class="brand-mark">velquora<sup>®</sup></div>

      <h1 class="product-title">Magnesium<span class="line-two">Komplex</span></h1>

      <div class="flower-ornament" role="img" aria-label="Dekorative hellgraue Blütenform mit sechs Blättern"></div>

      <div class="vegan-badge" role="img" aria-label="Vegan-Siegel"></div>
      <div class="capsule-count">365 KAPSELN</div>

      <div class="band-bottom"></div>
    </section>
  </main>
</body>
</html>
```